Fotograf sucht Gutschein-Design
Schnell, unkomplizierte Abwicklung und ich habe ein wunderschönes Design erhalten.
Zielgruppe
Bin Fotograf spezialisiert auf Pärchen und Hochzeitsfotos
Aufgabenstellung
Möchte einen neuen Gutschein für meine Zwecke haben. Sollte zu meinem fotografischen Stil passen, hell/ freundlich/ Retro? Vintage? Kann auch gerne 'Verzierung' mit Blümchen/ Zweige enthalten wenns passt. am besten ein wenig auf meiner Homepage orientieren >>> www.tobiasrandecker.com - Auch meine Logo/ Firmendaten sollten wo passend platziert sein. Mein Logo/ und Fotos füge ich bei und können wie es gut passt verwendet werden. Das auf dem Einzelbild bin ich, falls es wo passt wäre es toll. Schriftmäßig sollte es natürlich irgendwie das Wort Gutschein enthalten. Dann noch 'von' und 'für' und ein Feld wo ich händisch die Gutscheinnummer eintragen kann. Das Format/ Form überlasse ich auch ganz euch aber werde voraussichtlich bei karteneck bestellen. (Falls es um das finden des passenden Formats/ Form geht). Bei Fragen könnt ihr euch gerne jederzeit melden.

```html
<!DOCTYPE html>
<html lang="de">
<head>
<meta charset="utf-8">
<title>Gutschein – Tobias Randecker Fotografie</title>
<link rel="stylesheet" href="https://fonts.googleapis.com/css2?family=Great+Vibes&family=Roboto+Condensed:wght@300;400&family=Poppins:wght@300;600&display=swap">
<style>
  :root {
    --page: #ecebe8;
    --paper: #f4f1eb;
    --paper-deep: #efeae2;
    --ink: #1f1c19;
    --gold: #c4ad7f;
    --gold-soft: #e4d8bf;
    --olive: #8a7b5c;
    --field: #e6e2dc;
    --field-line: #2a2622;
    --shadow: rgba(0, 0, 0, 0.18);
  }
  * { box-sizing: border-box; margin: 0; padding: 0; }
  html, body { width: 1200px; height: 1200px; overflow: hidden; }
  body { background: var(--page); position: relative; font-family: "Poppins", sans-serif; color: var(--ink); }

  .voucher {
    position: absolute; left: 135px; width: 922px; height: 438px;
    background: var(--paper); overflow: hidden;
    box-shadow: 0 2px 6px var(--shadow);
  }
  .voucher--front { top: 149px; }
  .voucher--back { top: 615px; }

  .foliage { position: absolute; }
  .foliage--top-left {
    left: 40px; top: 0; width: 270px; height: 130px;
    background: radial-gradient(ellipse at 40% 30%, rgba(138,123,92,0.55), rgba(196,173,127,0.25) 55%, rgba(244,241,235,0) 75%);
  }
  .foliage--bottom-right {
    right: 40px; bottom: 0; width: 380px; height: 110px;
    background: radial-gradient(ellipse at 60% 70%, rgba(196,173,127,0.55), rgba(228,216,191,0.35) 55%, rgba(244,241,235,0) 78%);
  }
  .corner-lines { position: absolute; left: 0; top: 0; width: 922px; height: 438px; }

  .brand {
    position: absolute; left: 765px; top: 110px; width: 127px; text-align: center;
    font-family: "Roboto Condensed", sans-serif; font-weight: 400; color: var(--ink);
  }
  .brand__name { font-size: 13px; letter-spacing: 2px; line-height: 1.2; }
  .brand__sub { font-size: 9px; letter-spacing: 3px; margin-top: 4px; }
  .brand__dot { width: 10px; height: 10px; border-radius: 50%; background: var(--ink); margin: 0 auto 10px; }

  .title {
    font-family: "Great Vibes", cursive; font-weight: 400; color: var(--ink);
    position: absolute; white-space: nowrap; line-height: 1;
  }
  .voucher--front .title { left: 190px; top: 140px; font-size: 150px; }
  .subtitle {
    position: absolute; font-family: "Roboto Condensed", sans-serif; font-weight: 300;
    color: var(--gold); text-transform: uppercase; white-space: nowrap;
  }
  .voucher--front .subtitle { right: 189px; top: 266px; font-size: 21px; }

  .pattern {
    position: absolute; inset: 0;
    background: linear-gradient(135deg, var(--paper) 0%, var(--paper-deep) 50%, var(--paper) 100%);
  }
  .voucher--back .title { left: 30px; top: 30px; font-size: 92px; }
  .voucher--back .subtitle { left: 125px; top: 110px; font-size: 22px; }

  .fields { position: absolute; left: 31px; top: 155px; width: 566px; }
  .field {
    height: 49px; border: 1px solid var(--field-line); background: var(--field);
    padding: 5px 10px; font-size: 12px; font-weight: 300; margin-bottom: 32px;
  }
  .terms {
    position: absolute; left: 31px; top: 380px; width: 600px;
    font-family: "Roboto Condensed", sans-serif; font-weight: 300; font-size: 8.6px; line-height: 18px;
  }

  .portrait { position: absolute; left: 664px; top: 36px; width: 206px; height: 190px; }
  .portrait__photo {
    position: absolute; left: 8px; top: 8px; width: 190px; height: 174px;
    clip-path: polygon(25% 0, 75% 0, 100% 50%, 75% 100%, 25% 100%, 0 50%);
    background: linear-gradient(160deg, #c9cbc6 0%, #8e8a78 45%, #7d6a4e 80%, #a57b47 100%);
  }
  .portrait__frame { position: absolute; inset: 0; }

  .contacts { position: absolute; left: 669px; top: 248px; list-style: none; }
  .contacts li { display: flex; align-items: center; height: 18px; margin-bottom: 16px; font-size: 12.5px; font-weight: 600; }
  .contacts li:nth-child(3) { margin-bottom: 12px; }
  .contacts svg { width: 18px; height: 18px; margin-right: 10px; flex: none; }
</style>
</head>
<body>

<section class="voucher voucher--front">
  <div class="foliage foliage--top-left" role="img" aria-label="Zweige mit Blättern und Beeren in Oliv und Sand"></div>
  <div class="foliage foliage--bottom-right" role="img" aria-label="Goldener Palmzweig"></div>
  <svg class="corner-lines" viewBox="0 0 922 438" aria-hidden="true">
    <line x1="0" y1="98" x2="230" y2="0" stroke="var(--gold)" stroke-width="0.8"/>
    <line x1="0" y1="305" x2="155" y2="438" stroke="var(--gold)" stroke-width="0.8"/>
    <line x1="0" y1="325" x2="140" y2="438" stroke="var(--gold)" stroke-width="0.8"/>
    <circle cx="33" cy="58" r="3" fill="var(--gold-soft)"/>
    <circle cx="23" cy="376" r="3" fill="var(--gold)"/>
    <circle cx="148" cy="405" r="3" fill="var(--gold)"/>
    <circle cx="909" cy="13" r="3" fill="var(--gold)"/>
  </svg>
  <div class="brand">
    <div class="brand__dot"></div>
    <div class="brand__name">TOBIAS RANDECKER</div>
    <div class="brand__sub">FOTOGRAFIE</div>
  </div>
  <h1 class="title">Gutschein</h1>
  <p class="subtitle">Für ein Fotoshooting bei Tobias Randecker</p>
</section>

<section class="voucher voucher--back">
  <div class="pattern" role="img" aria-label="Zartes Muster aus hellen Palmblättern"></div>
  <h2 class="title">Gutschein</h2>
  <p class="subtitle">Für ein Fotoshooting</p>

  <div class="fields">
    <div class="field">Im Wert von:</div>
    <div class="field">Ausgestellt auf:</div>
    <div class="field">Gutscheinnr. &amp; Unterschrift:</div>
  </div>
  <p class="terms">*Einlösbar Online auf www.tobiasrandecker.com. Pro Bestellung ist ein Gutschein einlösbar. Eine Barablöse ist nicht möglich.<br>
  Gutscheine können fünf Jahre ab dem Erwerb (=Rechnungsdatum) eingelöst werden und verfallen nach diesem Zeitraum.</p>

  <div class="portrait">
    <div class="portrait__photo" role="img" aria-label="Porträt des Fotografen in herbstlicher Landschaft"></div>
    <svg class="portrait__frame" viewBox="0 0 206 190" aria-hidden="true">
      <polygon points="60,4 150,10 202,96 150,186 58,182 6,95" fill="none" stroke="var(--gold)" stroke-width="1.4"/>
      <polygon points="52,10 140,2 198,88 156,178 64,188 2,100" fill="none" stroke="var(--gold)" stroke-width="1"/>
    </svg>
  </div>

  <ul class="contacts">
    <li><svg viewBox="0 0 18 18" aria-hidden="true"><path d="M9 1.5a5 5 0 0 1 5 5c0 3.6-5 8.5-5 8.5s-5-4.9-5-8.5a5 5 0 0 1 5-5z" fill="none" stroke="var(--gold)" stroke-width="1.1"/><circle cx="9" cy="6.5" r="1.8" fill="none" stroke="var(--gold)" stroke-width="1.1"/><ellipse cx="9" cy="16" rx="6" ry="1.3" fill="none" stroke="var(--gold)" stroke-width="0.8"/></svg>Lindenweg 7 - 3920 Waldau</li>
    <li><svg viewBox="0 0 18 18" aria-hidden="true"><rect x="1.5" y="5" width="15" height="11" fill="none" stroke="var(--gold)" stroke-width="1.1"/><path d="M1.5 5l7.5 6 7.5-6M4 5V2h10v3" fill="none" stroke="var(--gold)" stroke-width="1.1"/></svg>info@tobiasrandecker.com</li>
    <li><svg viewBox="0 0 18 18" aria-hidden="true"><path d="M4 2l3 3-1.6 2c1 2 2.6 3.6 4.6 4.6l2-1.6 3 3-2 2.5C7.5 15 3 10.5 1.5 4z" fill="none" stroke="var(--gold)" stroke-width="1.1"/><path d="M10 1.5a6.5 6.5 0 0 1 6.5 6.5M10 4a4 4 0 0 1 4 4" fill="none" stroke="var(--gold)" stroke-width="1"/></svg>Handy: 0660 12 34 567</li>
    <li><svg viewBox="0 0 18 18" aria-hidden="true"><circle cx="9" cy="9" r="7.5" fill="none" stroke="var(--gold)" stroke-width="1.1"/><ellipse cx="9" cy="9" rx="3.2" ry="7.5" fill="none" stroke="var(--gold)" stroke-width="1"/><path d="M1.5 9h15M3 5h12M3 13h12" stroke="var(--gold)" stroke-width="1"/></svg>www.tobiasrandecker.com</li>
  </ul>
</section>

</body>
</html>
```